www.hollisbenchworks.com website

This is a company that was founded by my Great Great Grandfather in 1872. It was started in Detroit and moved to Calder Springs, Ohio. I am reviving the brand. We will sell licensed chairs, apparel, online appraisals for Hollis Benches from 1872-1954, and an ebook with history of the company.

Design a quality WordPress Website for www.hollisbenchworks.com that visually depicts the history and brand of this 145-year-old American chair manufacturing company that was founded in Detroit and refined in Owensboro but also has a freshness to a new lifestyle brand for today. It will be hosted on Hostpine with the following pages:

Our Story, Past and Present
Our People, 6 Generations of Hollis
Our Products and Services:
Chairs, Appraisals, Apparel, Hollis History eBook,
Contact us:

Tagline for the company:
The Original Hollis Bench Works
Since 1872
Detroit, Michigan
Calder Springs, Ohio

The progress of Hollis Bench remains attributable to these principles:
1--A “One Price” Policy.
2--Quality Chairs at Reasonable Cost.
3--Constant Integrity and Fair Dealing.

Good source for content information is
https://www.facebook.com/hollisbenchworks/
I want to use the colors of crimson and green because they represent key colors for the company. Can be transparent in places. Want to demonstrate the iconic history of the company through some of the older picture.

Target Market(s)

Current owners of hollis benches (google it) that want the background and history of their chairs and the feeling of being in an international community along with the growth potential to offer new products to a new generation.

Industry/Entity Type

It Company

Number of Pages Required

4 page

Font styles to use
Sans Serif

Colors
ec1f27
00a990

Requirements
Must have
• Plug in and set up for a store with products.
• Plug in form for uploading information for an appraisal of an exisitng chair. (have included a form example)
Nice to have
• Usage of the baseball team photo. in the "our people" section usage of the all the head shot pictures. usage of the factory pictures.

```html
<!DOCTYPE html>
<html lang="en">
<head>
<meta charset="utf-8">
<title>Hollis Bench Works</title>
<link href="https://fonts.googleapis.com/css2?family=Montserrat:wght@500;600;700&family=Questrial&display=swap" rel="stylesheet">
<style>
:root{
  --crimson:#ec1f27;
  --green:#00a990;
  --ink:#222222;
  --body:#555555;
  --line:#dcdcdc;
  --band:#f1f1f1;
  --footer:#4d4a49;
  --yellow:#e9c24a;
  --white:#ffffff;
}
*{box-sizing:border-box;margin:0;padding:0}
html,body{width:1200px;height:1200px;overflow:hidden;background:var(--white)}
body{font-family:"Questrial",sans-serif;color:var(--ink);position:relative}
.page{position:absolute;left:350.4px;top:0;width:625px;height:1500px;transform:scale(.8);transform-origin:0 0;background:var(--white);overflow:hidden}
.abs{position:absolute}
.heading{font-family:"Montserrat",sans-serif;font-weight:600;font-size:11px;letter-spacing:.2px;color:var(--ink);text-transform:uppercase}
.btn{position:absolute;background:var(--crimson);color:var(--white);font-family:"Montserrat",sans-serif;font-weight:700;font-size:5.5px;text-transform:uppercase;display:flex;align-items:center;justify-content:center;letter-spacing:.2px}

/* header */
.topline{left:0;top:0;width:625px;height:3px;background:var(--crimson)}
.header{left:0;top:3px;width:625px;height:62px;background:var(--white)}
.brand{left:36px;top:0;width:88px;height:93px;background:var(--white);border:1.5px solid var(--crimson);border-top:none;z-index:3;display:flex;flex-direction:column;align-items:center;padding-top:12px}
.brand-dot{width:38px;height:38px;border-radius:50%;background:#6b6b6b}
.brand-name{margin-top:8px;font-size:7px;color:#333;text-align:center;line-height:1.15}
.brand-place{font-size:4.5px;color:#333;margin-top:2px}
.nav a{position:absolute;top:33px;font-family:"Montserrat",sans-serif;font-weight:500;font-size:7px;color:#333;text-decoration:none;white-space:nowrap}
.nav a.active{color:var(--crimson)}

/* hero */
.hero{left:0;top:65px;width:625px;height:289px;background:linear-gradient(180deg,#f3f0ec 0%,#ece6df 55%,#b9a699 72%,#5a3b32 82%,#cdb8a6 100%)}
.hero-arrow{top:181px;width:17px;height:32px;background:#2a2a2a;display:flex;align-items:center;justify-content:center}
.principle{top:312px;width:126px;height:126px;border-radius:50%;display:flex;align-items:center;justify-content:center;z-index:2}
.principle .inner{width:116px;height:116px;border-radius:50%;border:1.5px solid var(--white);display:flex;flex-direction:column;align-items:center;justify-content:center;color:var(--white);font-family:"Montserrat",sans-serif;font-weight:600;font-size:6px;line-height:1.9;text-align:center}
.principle svg{margin-bottom:6px}
.red{background:var(--crimson)}
.green{background:var(--green)}

/* best sellers */
.card{top:508px;width:126px;height:132px;border:2px solid var(--line);background:var(--white)}
.card .photo{position:absolute;left:28px;top:14px;width:66px;height:86px;border-radius:4px}
.card .name{position:absolute;left:0;right:0;top:107px;text-align:center;font-family:"Montserrat",sans-serif;font-weight:600;font-size:7.5px;color:#222}
.chev{font-family:"Montserrat",sans-serif;font-size:14px;color:#333}

/* history */
.history-left{left:0;top:685px;width:280px;height:238px;background:linear-gradient(180deg,#ecc64f 0%,#e6bb3a 100%)}
.history-right{left:280px;top:685px;width:345px;height:238px;background:linear-gradient(135deg,#f4f2ef 0%,#e2ded9 45%,#d6a56a 65%,#3f8a86 80%,#d9d4cf 100%)}
.history-text{left:40px;top:730px;width:234px;font-size:6.2px;line-height:13px;color:#4a3d14}

/* contact band */
.band{left:0;top:923px;width:625px;height:97px;background:var(--band)}

/* gallery */
.thumb{width:111px;height:90px;background:var(--white);border:1px solid #e5e5e5;box-shadow:0 1px 3px rgba(0,0,0,.12);padding:4px}
.thumb div{width:100%;height:100%}

/* testimonials */
.quote-mark{font-family:"Montserrat",sans-serif;font-weight:700;font-size:18px;color:#bdbdbd;line-height:1}
.testimonial-text{left:360px;top:1082px;width:170px;font-size:6.5px;line-height:13px;color:#555}
.avatar{left:396px;top:1118px;width:90px;height:90px;border-radius:50%;background:radial-gradient(circle at 50% 40%,#8fc3ea 0%,#4b94d3 60%,#2f6ea8 100%)}
.dot{top:1263px;width:5px;height:5px;border-radius:50%;background:#222}
.dot.muted{background:#999}

/* footer */
.footer{left:0;top:1304px;width:625px;height:196px;background:var(--footer)}
.footer-brand{left:38px;top:1318px;width:128px;display:flex;flex-direction:column;align-items:center;color:var(--white)}
.footer-brand .mark{width:66px;height:66px;border-radius:50%;background:#e9e9e9}
.footer-brand .name{margin-top:12px;font-size:12px}
.footer-brand .place{margin-top:3px;font-size:7px}
.footer-heading{color:var(--white)}
.footer-text{left:200px;top:1347px;width:220px;font-size:6.2px;line-height:13px;color:#ededed}
.field{left:441px;width:137px;height:18px;background:var(--white);font-size:6px;color:#aaa;padding:6px 0 0 6px}
.footer-link{top:1432px;font-family:"Montserrat",sans-serif;font-weight:600;font-size:5.8px;color:var(--white);white-space:nowrap}
.footer-small{top:1472px;font-family:"Montserrat",sans-serif;font-weight:500;font-size:5.2px;color:var(--white);white-space:nowrap}
.bottomline{left:0;top:1497px;width:625px;height:3px;background:var(--crimson)}
</style>
</head>
<body>
<div class="page">

  <!-- header -->
  <div class="abs topline"></div>
  <div class="abs header"></div>
  <div class="abs brand">
    <div class="brand-dot"></div>
    <div class="brand-name">Hollis Bench Works</div>
    <div class="brand-place">Calder Springs, Ohio</div>
  </div>
  <nav class="nav">
    <a class="active" style="left:158px">Home</a>
    <a style="left:207px">Our Story</a>
    <a style="left:268px">Our People</a>
    <a style="left:337px">Products &amp; Services</a>
    <a style="left:437px">Chairs &amp; Appraisals</a>
    <a style="left:537px">Contact us</a>
  </nav>

  <!-- hero -->
  <div class="abs hero" role="img" aria-label="Bright living room with a brown leather sofa, armchair and ottoman beside tall windows"></div>
  <div class="abs hero-arrow" style="left:0">
    <svg width="8" height="12" viewBox="0 0 8 12"><path d="M6 1 1 6l5 5" fill="none" stroke="#fff" stroke-width="1.2"/></svg>
  </div>
  <div class="abs hero-arrow" style="left:608px">
    <svg width="8" height="12" viewBox="0 0 8 12"><path d="M2 1l5 5-5 5" fill="none" stroke="#fff" stroke-width="1.2"/></svg>
  </div>

  <div class="abs principle red" style="left:111px">
    <div class="inner">
      <svg width="30" height="30" viewBox="0 0 30 30"><path d="M6 18 17 7l7 1 1 7-11 11z" fill="none" stroke="#fff" stroke-width="2" stroke-linejoin="round"/><circle cx="20.5" cy="11.5" r="2" fill="none" stroke="#fff" stroke-width="1.6"/></svg>
      <span>A “One Price”<br>Policy</span>
    </div>
  </div>
  <div class="abs principle green" style="left:259px">
    <div class="inner">
      <svg width="30" height="30" viewBox="0 0 30 30"><circle cx="15" cy="15" r="12.5" fill="none" stroke="#fff" stroke-width="2"/><path d="M9 14h3v8H9zM13 14l3-6c2 0 2 2 1.5 4H21c1 0 1.5 1 1 2l-1.5 6c-.3.8-1 1-1.8 1H13z" fill="none" stroke="#fff" stroke-width="1.6" stroke-linejoin="round"/></svg>
      <span>Quality Chairs<br>at Reasonable Cost</span>
    </div>
  </div>
  <div class="abs principle green" style="left:405px">
    <div class="inner">
      <svg width="34" height="30" viewBox="0 0 34 30"><path d="M2 10l6-4 6 3 6-3 6 2 6 5M8 6l-4 10 10 8c1.5 1 3 0 2.5-1.5M26 8l4 9-8 7" fill="none" stroke="#fff" stroke-width="2" stroke-linejoin="round" stroke-linecap="round"/><path d="M14 9l-4 4c1 1.5 3 1.5 4 0l2-2 7 7" fill="none" stroke="#fff" stroke-width="1.8" stroke-linejoin="round"/></svg>
      <span>Constant Integrity<br>&amp; Fair Dealing</span>
    </div>
  </div>

  <!-- best sellers -->
  <h2 class="abs heading" style="left:37px;top:478px">Best Sellers</h2>
  <div class="abs chev" style="left:15px;top:559px">‹</div>
  <div class="abs chev" style="left:589px;top:559px">›</div>
  <div class="abs card" style="left:38px">
    <div class="photo" role="img" aria-label="Wooden ladder-back dining chair" style="background:linear-gradient(180deg,#e4cfae,#c9a97c)"></div>
    <div class="name">Carrow Chair Model 1</div>
  </div>
  <div class="abs card" style="left:177px">
    <div class="photo" role="img" aria-label="Oak chair with upholstered seat" style="background:linear-gradient(180deg,#e2cfb0,#c6a37c)"></div>
    <div class="name">Lark Chair</div>
  </div>
  <div class="abs card" style="left:315px">
    <div class="photo" role="img" aria-label="White shell chair on steel legs" style="background:linear-gradient(180deg,#eeeeee,#c9c9c9)"></div>
    <div class="name">Carrow Chair</div>
  </div>
  <div class="abs card" style="left:453px">
    <div class="photo" role="img" aria-label="Brown tufted armchair" style="background:linear-gradient(180deg,#9a7357,#6b4a35)"></div>
    <div class="name">Chair Sofa</div>
  </div>

  <!-- history -->
  <div class="abs history-left" role="img" aria-label="Yellow tinted interior with a woven basket"></div>
  <div class="abs history-right" role="img" aria-label="Grey sofa with patterned cushions and a yellow chair"></div>
  <h2 class="abs heading" style="left:38px;top:700px">Our History</h2>
  <p class="abs history-text">The history of the Hollis Bench Company is as rich as it is long. M.J. Hollis was a young entrepreneur that began the Hollis business at the young age of 20 in what would eventually grow at its peak to become the largest chair manufacturing company in the world. He would go on to become a leading manufacturer of his time and founding member of the Riverside Merchants Guild as well as a member of the board of a young Lakeshore Motors Company.</p>
  <div class="btn" style="left:201px;top:842px;width:70px;height:20px;border-radius:3px">Read More</div>

  <!-- contact band -->
  <div class="abs band"></div>
  <h2 class="abs heading" style="left:0;width:660px;text-align:center;top:943px">For More Information Contact Us</h2>
  <div class="btn" style="left:299px;top:975px;width:69px;height:21px">Contact Us</div>

  <!-- gallery -->
  <h2 class="abs heading" style="left:38px;top:1038px">Gallery</h2>
  <div class="abs thumb" style="left:38px;top:1067px"><div role="img" aria-label="Rows of classic chairs on a riverside promenade" style="background:linear-gradient(180deg,#5f96d6 0%,#8db6e2 50%,#5b6f86 100%)"></div></div>
  <div class="abs thumb" style="left:158px;top:1067px"><div role="img" aria-label="Chairs set out under a bridge pavilion" style="background:linear-gradient(180deg,#c9c3b8 0%,#8f8b84 50%,#6f5e4e 100%)"></div></div>
  <div class="abs thumb" style="left:38px;top:1162px"><div role="img" aria-label="Historic view of the chair factory" style="background:linear-gradient(180deg,#cfc4b2 0%,#9c8d78 60%,#6d604f 100%)"></div></div>
  <div class="abs thumb" style="left:158px;top:1162px"><div role="img" aria-label="Vintage photo of the company baseball team" style="background:linear-gradient(180deg,#9a9a9a 0%,#6d6d6d 60%,#4a4a4a 100%)"></div></div>
  <div class="btn" style="left:44px;top:1265px;width:52px;height:19px">View More</div>

  <!-- testimonials -->
  <h2 class="abs heading" style="left:291px;top:1038px">Testimonials</h2>
  <div class="abs quote-mark" style="left:335px;top:1069px">“</div>
  <p class="abs testimonial-text">Lorem Ipsum is simply dummy text of the printing and typesetting industry.</p>
  <div class="abs quote-mark" style="left:464px;top:1097px">”</div>
  <svg class="abs" style="left:306px;top:1157px" width="8" height="12" viewBox="0 0 8 12"><path d="M6 1 1 6l5 5" fill="none" stroke="#555" stroke-width="2"/></svg>
  <svg class="abs" style="left:555px;top:1157px" width="8" height="12" viewBox="0 0 8 12"><path d="M2 1l5 5-5 5" fill="none" stroke="#555" stroke-width="2"/></svg>
  <div class="abs avatar" role="img" aria-label="Customer portrait outdoors under a blue sky"></div>
  <div class="abs" style="left:341px;width:200px;top:1221px;text-align:center;font-family:'Montserrat',sans-serif;font-weight:600;font-size:8px">Sed ut perspiciatis</div>
  <div class="abs dot" style="left:430px"></div>
  <div class="abs dot muted" style="left:437px"></div>
  <div class="abs dot" style="left:445px"></div>

  <!-- footer -->
  <div class="abs footer"></div>
  <div class="abs footer-brand">
    <div class="mark"></div>
    <div class="name">Hollis Bench Works</div>
    <div class="place">Calder Springs, Ohio</div>
  </div>
  <h2 class="abs heading footer-heading" style="left:199px;top:1319px">Our Story</h2>
  <p class="abs footer-text">The history of the Hollis Bench Company is as rich as it is long. M.J. Hollis was a young entrepreneur that began the Hollis business at the young age of 20 in what would eventually grow at its peak to become the largest chair manufacturing company in the world.</p>
  <h2 class="abs heading footer-heading" style="left:440px;top:1319px">Contact Us</h2>
  <div class="abs field" style="top:1346px">Name</div>
  <div class="abs field" style="top:1369px">Email Id</div>
  <div class="abs" style="left:441px;top:1392px;width:64px;height:18px;background:var(--crimson);color:#fff;font-family:'Montserrat',sans-serif;font-weight:600;font-size:7.5px;display:flex;align-items:center;justify-content:center">Send Now</div>
  <span class="abs footer-link" style="left:200px">Home</span>
  <span class="abs footer-link" style="left:240px">Returns &amp; Exchanges</span>
  <span class="abs footer-link" style="left:327px">Shipping Charges</span>
  <span class="abs footer-link" style="left:404px">International Shipping Policy</span>
  <span class="abs footer-link" style="left:514px">Contact US</span>
  <span class="abs footer-small" style="left:38px">Privacy Policy</span>
  <span class="abs footer-small" style="left:89px">Terms &amp; Conditions</span>
  <span class="abs footer-small" style="right:48px">All Copy Rights Reserved © hollisbenchworks.com</span>
  <div class="abs bottomline"></div>
</div>
</body>
</html>
```